Quality Improvement Software for healthcare agencies needs a website.

VORTEL218 is a software for hospices and home health agencies to manage their Quality Assurance Performance Improvement programs to remain complaint with the standards set by Sanavox and the Bureau of Clinical Oversight. The web accessible software-as-a-service provides an easy, turn-key way for agencies to organize all the information they need to manage and track.

Coding

Coded - Design and coding required

Number of Pages Required

4 page

```html
<!DOCTYPE html>
<html lang="en">
<head>
<meta charset="utf-8">
<title>VORTEL218 — Quality Improvement Software for Healthcare Agencies</title>
<link href="https://fonts.googleapis.com/css2?family=Inter:wght@400;500;600;700;800&display=swap" rel="stylesheet">
<style>
:root{
  --bg:#0b0a22;
  --orange:#f7931e;
  --white:#ffffff;
  --muted:#c9c8d8;
  --navy-card:#213b8c;
  --ink:#17163a;
  --grey-text:#8d8ca3;
  --lavender:#ecebfb;
  --line:#3a3960;
}
*{box-sizing:border-box;margin:0;padding:0}
html,body{width:1200px;height:3922px;overflow:hidden}
body{
  position:relative;
  font-family:"Inter",sans-serif;
  color:var(--white);
  background:
    radial-gradient(ellipse 380px 260px at 0px 470px, rgba(214,88,30,.45), transparent 70%),
    radial-gradient(ellipse 520px 360px at 1050px 200px, rgba(70,40,110,.35), transparent 70%),
    radial-gradient(ellipse 700px 420px at 600px 1000px, rgba(40,30,120,.45), transparent 70%),
    radial-gradient(ellipse 600px 400px at 400px 1750px, rgba(40,30,120,.35), transparent 70%),
    var(--bg);
}
.block{position:absolute;left:0;width:1200px}
.pill{display:inline-block;border:1.5px solid var(--orange);border-radius:20px;color:var(--white);font-size:12px;padding:5px 16px}

/* header */
.site-header{top:0;height:73px}
.brand-plate{position:absolute;left:0;top:0;width:260px;height:73px;background:#eeeef2;clip-path:polygon(0 0,100% 0,81% 100%,0 100%)}
.brand{position:absolute;left:36px;top:20px;display:flex;align-items:center;gap:8px;font-size:27px;font-weight:800;color:#1e2a6b;letter-spacing:.3px}
.brand-mark{width:22px;height:22px;background:var(--orange);border-radius:4px}
.main-nav{position:absolute;left:472px;top:29px;display:flex;gap:18px;font-size:11px}
.auth{position:absolute;right:38px;top:28px;display:flex;gap:24px;font-size:11px}

/* hero */
.hero{top:120px;text-align:center}
.hero h1{margin-top:22px;font-size:39px;line-height:50px;font-weight:700}
.hero p{margin-top:16px;font-size:11.5px;line-height:21px;color:var(--muted)}
.dashboard{position:absolute;left:297px;top:220px;width:605px;height:357px;border-radius:16px;
  background:linear-gradient(160deg,#0f1a2a,#07101a 60%,#0b1420);box-shadow:0 0 0 4px #1a1c26}

/* features */
.features{top:775px;text-align:center}
.features h2{margin-top:24px;font-size:31px;line-height:46px;font-weight:700}
.feature-grid{position:absolute;top:170px;left:84px;width:1040px;display:grid;grid-template-columns:384px 377px 280px;row-gap:48px;text-align:left}
.feature{display:flex;gap:16px}
.feature-icon{flex:0 0 68px;height:68px;border-radius:8px;background:#2a2940;display:flex;align-items:center;justify-content:center}
.feature h3{font-size:13.5px;font-weight:600;margin-bottom:10px}
.feature p{font-size:10.5px;line-height:24px;color:var(--muted)}

/* about */
.about{top:1310px}
.about-text{position:absolute;left:38px;width:540px}
.about .pill{width:130px;text-align:center}
.about h2{margin-top:18px;font-size:30px;line-height:39px;font-weight:700}
.about p.lead{margin-top:20px;font-size:12.5px;line-height:27.5px;color:var(--muted)}
.check-list{list-style:none;margin-top:10px}
.check-list li{display:flex;gap:12px;font-size:12.5px;line-height:27px;margin-bottom:10px;color:var(--muted)}
.half-dot{flex:0 0 20px;height:20px;margin-top:4px;border-radius:50%;border:2px solid #fff;background:linear-gradient(90deg,#fff 50%,transparent 50%)}
.about-art{position:absolute;left:599px;top:-8px;width:532px;height:380px;border-radius:10px;
  background:radial-gradient(circle at 55% 45%,#f4c542 0 18%,#2c5fd6 19% 38%,transparent 60%),linear-gradient(180deg,#141540,#0d0c2a)}

/* pricing */
.pricing{top:1812px;text-align:center}
.pricing h2{margin-top:12px;font-size:42px;font-weight:700}
.plans{position:absolute;top:145px;left:84px;display:flex;gap:26px}
.plan{width:327px;height:548px;border-radius:12px;background:var(--white);color:var(--ink);padding:40px 18px 40px 36px;text-align:left}
.plan.featured{background:var(--navy-card);color:var(--white);border:1.5px solid #4d67c4}
.plan-head{display:flex;gap:14px;align-items:center}
.plan-icon{width:60px;height:60px;border-radius:10px;background:var(--lavender);display:flex;align-items:center;justify-content:center}
.plan-icon span{width:28px;height:28px;border-radius:50%;border:2.5px solid #17163a;background:linear-gradient(90deg,var(--orange) 50%,#17163a 50%)}
.plan-for{font-size:13.5px;color:var(--grey-text)}
.featured .plan-for{color:#dfe4f7}
.plan-name{font-size:19px;font-weight:700;margin-top:3px}
.plan-note{margin-top:26px;width:255px;font-size:17px;line-height:25px;color:var(--grey-text)}
.featured .plan-note{color:#e2e6f6}
.price{margin-top:16px;font-size:44px;font-weight:700;letter-spacing:-.5px}
.featured .price{color:var(--orange)}
.price small{font-size:16px;font-weight:400;color:var(--grey-text);margin-left:8px}
.featured .price small{color:#e2e6f6}
.included{margin-top:16px;font-size:15px;font-weight:700}
.perks{list-style:none;margin-top:18px}
.perks li{display:flex;align-items:center;gap:12px;font-size:12.5px;height:35px;white-space:nowrap}
.tick{width:21px;height:21px;border-radius:50%;background:var(--orange);display:flex;align-items:center;justify-content:center;flex:0 0 21px}
.btn{display:flex;align-items:center;justify-content:center;background:var(--orange);color:var(--white);font-weight:600;font-size:14px;border-radius:30px}
.plan .btn{margin-top:26px;height:60px;width:255px}

/* download */
.download{top:2604px;left:37px;width:1123px;height:667px;border:1px solid var(--line);border-radius:4px}
.download-text{position:absolute;left:65px;top:72px;width:545px}
.download h2{font-size:30px;line-height:39px;font-weight:700}
.download p.lead{margin-top:24px;font-size:12px;line-height:27.5px;color:var(--muted)}
.download .check-list{margin-top:20px}
.download .check-list li{font-size:12px}
.download .btn{width:257px;height:58px;margin-top:22px;font-size:14px}
.phone{position:absolute;left:700px;top:-10px;width:280px;height:560px;border-radius:40px;transform:rotate(-14deg);
  background:linear-gradient(160deg,#2a2d34,#0a0d12 40%,#0d2a3a 70%,#1a1d24)}

/* newsletter */
.newsletter{top:3239px;left:84px;width:1032px;height:230px;background:var(--white);color:var(--ink);border-radius:4px}
.nl-icon{position:absolute;left:50px;top:60px}
.newsletter h2{position:absolute;left:126px;top:42px;font-size:37px;font-weight:600}
.newsletter p{position:absolute;left:127px;top:104px;width:365px;font-size:11.5px;line-height:29px}
.nl-form{position:absolute;left:553px;top:92px;display:flex}
.nl-form .field{width:338px;height:44px;background:#e2e2e6;color:#a7a7b2;font-size:12px;display:flex;align-items:center;padding-left:18px}
.nl-form .send{width:88px;height:44px;background:var(--orange);color:var(--white);font-weight:700;font-size:15px;display:flex;align-items:center;justify-content:center}

/* footer */
.site-footer{top:3520px;height:402px}
.foot-col{position:absolute;top:0}
.foot-col h4{font-size:16px;font-weight:500;padding-bottom:16px;margin-bottom:18px;position:relative}
.foot-col h4::after{content:"";position:absolute;left:0;bottom:0;width:140px;height:1.5px;background:var(--orange)}
.foot-col ul{list-style:none}
.foot-col li{font-size:12px;height:36px}
.foot-about p{font-size:12px;line-height:32.5px;width:330px}
.socials{display:flex;gap:10px;margin-top:14px}
.socials span{width:16px;height:16px;border-radius:50%;border:1.8px solid #fff}
.foot-bottom{position:absolute;top:340px;left:0;width:1200px;border-top:1px solid #2a2946;font-size:12px}
.foot-bottom .copy{position:absolute;left:184px;top:26px}
.foot-bottom .legal{position:absolute;left:812px;top:26px;display:flex;gap:20px}
</style>
</head>
<body>

<header class="block site-header">
  <div class="brand-plate"></div>
  <div class="brand"><span class="brand-mark"></span>VORTEL218</div>
  <nav class="main-nav"><span>Product</span><span>Pricing</span><span>About</span><span>Resources</span><span>Download</span></nav>
  <div class="auth"><span>Log In</span><span>Sign Up</span></div>
</header>

<section class="block hero">
  <span class="pill">Empowering Healthcare Agencies</span>
  <h1>Seamlessly Manage and Track<br>with VORTEL218</h1>
  <p>Unlock Effortless Compliance Management - A Web-Accessible<br>Turn-Key Solution for Organizing Vital Information</p>
  <div class="dashboard" role="img" aria-label="Analytics dashboard showing load time versus bounce rate charts and page view metrics"></div>
</section>

<section class="block features">
  <span class="pill">Key Features</span>
  <h2>"Unlocking Excellence: Key Features<br>of ClinivaTrack360"</h2>
  <div class="feature-grid">
    <div class="feature"><div class="feature-icon"><svg width="30" height="30" viewBox="0 0 30 30"><circle cx="15" cy="15" r="13" fill="none" stroke="#fff" stroke-width="2"/><path d="M9 15.5l4 4 8-9" fill="none" stroke="#fff" stroke-width="2.2"/></svg></div><div><h3>Comprehensive Oversight</h3><p>"Strategic Decision-Making Made<br>Easy - Gain a 360° View of Your<br>QAPI Programs"</p></div></div>
    <div class="feature"><div class="feature-icon"><svg width="30" height="30" viewBox="0 0 30 30"><circle cx="15" cy="15" r="13" fill="none" stroke="#fff" stroke-width="2"/><path d="M9 15.5l4 4 8-9" fill="none" stroke="#fff" stroke-width="2.2"/></svg></div><div><h3>Turn-Key Accessibility</h3><p>"Anytime, Anywhere Management<br>- Web Accessibility for Effortless<br>Tracking and Oversight"</p></div></div>
    <div class="feature"><div class="feature-icon"><svg width="30" height="30" viewBox="0 0 30 30"><circle cx="15" cy="15" r="13" fill="none" stroke="#fff" stroke-width="2"/><path d="M9 15.5l4 4 8-9" fill="none" stroke="#fff" stroke-width="2.2"/></svg></div><div><h3>Customisable Solutions</h3><p>"Tailored to Your Needs -<br>Personalize ClinivaTrack360 for<br>a Unique QAPI Management"</p></div></div>
    <div class="feature"><div class="feature-icon"><svg width="30" height="30" viewBox="0 0 30 30"><circle cx="15" cy="15" r="13" fill="none" stroke="#fff" stroke-width="2"/><path d="M9 15.5l4 4 8-9" fill="none" stroke="#fff" stroke-width="2.2"/></svg></div><div><h3>Compliance Assurance</h3><p>"Stay Ahead with Confidence -<br>Effortless Compliance with<br>Sanavox and Health Services<br>Standards"</p></div></div>
    <div class="feature"><div class="feature-icon"><svg width="30" height="30" viewBox="0 0 30 30"><circle cx="15" cy="15" r="13" fill="none" stroke="#fff" stroke-width="2"/><path d="M9 15.5l4 4 8-9" fill="none" stroke="#fff" stroke-width="2.2"/></svg></div><div><h3>Efficiency Unleashed</h3><p>"Save Time, Save Resources -<br>Unparalleled Efficiency in QAPI<br>Program Management"</p></div></div>
    <div class="feature"><div class="feature-icon"><svg width="30" height="30" viewBox="0 0 30 30"><circle cx="15" cy="15" r="13" fill="none" stroke="#fff" stroke-width="2"/><path d="M9 15.5l4 4 8-9" fill="none" stroke="#fff" stroke-width="2.2"/></svg></div><div><h3>User-Friendly Interface</h3><p>"Simplicity at Every Click - Intuitive<br>Design for Users of All Levels,<br>Minimizing the Learning Curve"</p></div></div>
  </div>
</section>

<section class="block about">
  <div class="about-text">
    <span class="pill">About us</span>
    <h2>Streamlined Compliance<br>Management</h2>
    <p class="lead">ClinivaTrack360 empowers healthcare agencies with a turn-key solution for efficient organization and tracking of essential information. Say goodbye to the complexities of compliance management, as our user-friendly platform provides a straightforward approach to meeting and exceeding industry standards.</p>
    <ul class="check-list">
      <li><span class="half-dot"></span>Dedicating ourselves to revolutionizing healthcare management through<br>innovative solutions.</li>
      <li><span class="half-dot"></span>Committed to delivering exceptional service, tailored to the unique needs of<br>healthcare agencies.</li>
    </ul>
  </div>
  <div class="about-art" role="img" aria-label="Illustration of a healthcare worker beside a clipboard, medical shield, heart and thermometer"></div>
</section>

<section class="block pricing">
  <span class="pill" style="padding:5px 44px">Pricing</span>
  <h2>Our Pricing Plans</h2>
  <div class="plans">
    <article class="plan">
      <div class="plan-head"><div class="plan-icon"><span></span></div><div><div class="plan-for">For individuals</div><div class="plan-name">Basic</div></div></div>
      <p class="plan-note">All plans come with a [30-day free trial]</p>
      <div class="price">$99<small>/monthly</small></div>
      <div class="included">What’s included</div>
      <ul class="perks">
        <li><span class="tick"><svg width="11" height="11" viewBox="0 0 11 11"><path d="M2 5.5l2.3 2.3L9 3" fill="none" stroke="#fff" stroke-width="1.8"/></svg></span>Ideal for Small Agencies</li>
        <li><span class="tick"><svg width="11" height="11" viewBox="0 0 11 11"><path d="M2 5.5l2.3 2.3L9 3" fill="none" stroke="#fff" stroke-width="1.8"/></svg></span>Affordable entry-level pricing</li>
        <li><span class="tick"><svg width="11" height="11" viewBox="0 0 11 11"><path d="M2 5.5l2.3 2.3L9 3" fill="none" stroke="#fff" stroke-width="1.8"/></svg></span>Essential features for getting started</li>
        <li><span class="tick"><svg width="11" height="11" viewBox="0 0 11 11"><path d="M2 5.5l2.3 2.3L9 3" fill="none" stroke="#fff" stroke-width="1.8"/></svg></span>Up to 3 team members</li>
      </ul>
      <div class="btn">Get started</div>
    </article>
    <article class="plan featured">
      <div class="plan-head"><div class="plan-icon"><span></span></div><div><div class="plan-for">For Startups</div><div class="plan-name">Pro</div></div></div>
      <p class="plan-note">All plans come with a [30-day free trial]</p>
      <div class="price">$199<small>/monthly</small></div>
      <div class="included">What’s included</div>
      <ul class="perks">
        <li><span class="tick"><svg width="11" height="11" viewBox="0 0 11 11"><path d="M2 5.5l2.3 2.3L9 3" fill="none" stroke="#fff" stroke-width="1.8"/></svg></span>Popular Choice for Growing Agencies</li>
        <li><span class="tick"><svg width="11" height="11" viewBox="0 0 11 11"><path d="M2 5.5l2.3 2.3L9 3" fill="none" stroke="#fff" stroke-width="1.8"/></svg></span>Affordable for Startups</li>
        <li><span class="tick"><svg width="11" height="11" viewBox="0 0 11 11"><path d="M2 5.5l2.3 2.3L9 3" fill="none" stroke="#fff" stroke-width="1.8"/></svg></span>Accommodate growing agencies</li>
        <li><span class="tick"><svg width="11" height="11" viewBox="0 0 11 11"><path d="M2 5.5l2.3 2.3L9 3" fill="none" stroke="#fff" stroke-width="1.8"/></svg></span>Up to 10 team members</li>
      </ul>
      <div class="btn">Get started</div>
    </article>
    <article class="plan">
      <div class="plan-head"><div class="plan-icon"><span></span></div><div><div class="plan-for">For Big Companies</div><div class="plan-name">Enterprise</div></div></div>
      <p class="plan-note">All plans come with a [30-day free trial]</p>
      <div class="price">$399<small>/monthly</small></div>
      <div class="included">What’s included</div>
      <ul class="perks">
        <li><span class="tick"><svg width="11" height="11" viewBox="0 0 11 11"><path d="M2 5.5l2.3 2.3L9 3" fill="none" stroke="#fff" stroke-width="1.8"/></svg></span>Enterprise-level Solution</li>
        <li><span class="tick"><svg width="11" height="11" viewBox="0 0 11 11"><path d="M2 5.5l2.3 2.3L9 3" fill="none" stroke="#fff" stroke-width="1.8"/></svg></span>Advanced QAPI Management</li>
        <li><span class="tick"><svg width="11" height="11" viewBox="0 0 11 11"><path d="M2 5.5l2.3 2.3L9 3" fill="none" stroke="#fff" stroke-width="1.8"/></svg></span>Customization options</li>
        <li><span class="tick"><svg width="11" height="11" viewBox="0 0 11 11"><path d="M2 5.5l2.3 2.3L9 3" fill="none" stroke="#fff" stroke-width="1.8"/></svg></span>Up to 3 team members</li>
      </ul>
      <div class="btn">Get started</div>
    </article>
  </div>
</section>

<section class="block download">
  <div class="phone" role="img" aria-label="Mobile phone displaying the analytics dashboard"></div>
  <div class="download-text">
    <h2>Elevate Your QAPI Experience -<br>Download ClinivaTrack360<br>Today!</h2>
    <p class="lead">At ClinivaTrack360, we're excited to offer you a seamless experience in managing your Quality Assurance Performance Improvement (QAPI) programs. Download our software to streamline compliance management, enhance efficiency, and elevate the quality of healthcare services your agency provides.</p>
    <ul class="check-list">
      <li><span class="half-dot"></span>Get started by downloading our user-friendly software for your desktop or<br>mobile device.</li>
      <li><span class="half-dot"></span>Experience the convenience of web accessibility, allowing you to manage and<br>track from anywhere.</li>
    </ul>
    <div class="btn">Download Mobile App</div>
  </div>
</section>

<section class="block newsletter">
  <svg class="nl-icon" width="56" height="50" viewBox="0 0 56 50"><rect x="14" y="2" width="40" height="28" rx="3" fill="#f7931e"/><path d="M14 4l20 14 20-14" fill="none" stroke="#fff" stroke-width="2"/><rect x="2" y="20" width="40" height="28" rx="3" fill="#f7931e" stroke="#fff" stroke-width="2"/><path d="M3 22l19 13 19-13" fill="none" stroke="#fff" stroke-width="2"/></svg>
  <h2>Newsletter</h2>
  <p>Your source for the latest updates, industry insights, and tips<br>to enhance your healthcare agency's compliance and<br>performance.</p>
  <div class="nl-form"><div class="field">Your E-Mail</div><div class="send">SEND</div></div>
</section>

<footer class="block site-footer">
  <div class="foot-col foot-about" style="left:134px">
    <h4 style="margin-left:3px">About us</h4>
    <p>We are dedicated to revolutionizing the way<br>healthcare agencies manage Quality Assurance<br>Performance Improvement (QAPI) programs. With a<br>commitment to simplicity and compliance. we provide<br>innovative solutions tailored to the unique needs of<br>hospices and home health agencies.</p>
    <div class="socials"><span></span><span></span><span></span></div>
  </div>
  <div class="foot-col" style="left:556px">
    <h4>Resources</h4>
    <ul><li>Home</li><li>About</li><li>Download</li><li>Key Features</li><li>Pricing</li><li>Contact Us</li></ul>
  </div>
  <div class="foot-col" style="left:850px;top:3px">
    <h4>Other Links</h4>
    <ul><li>Comprehensive Oversight</li><li>Turn-Key Accessibility</li><li>Customisable Solutions</li><li>Compliance Assurance</li><li>Efficiency Unleashed</li><li>User-Friendly Interface</li></ul>
  </div>
  <div class="foot-bottom">
    <span class="copy">Copyright by VORTEL218</span>
    <span class="legal"><span>Privacy Policy</span><span>Legal Agreement</span></span>
  </div>
</footer>

</body>
</html>
```